Professional/Sleek card design for athletic apparel brand

Athletic apparel brand. Mainly focused on lifting weights/gym workouts. Logo and brand are already created. Must use brand logo and name. Creativity is welcome. Looking for a clean, modern, and sexy design.

```html
<!DOCTYPE html>
<html lang="en">
<head>
<meta charset="utf-8">
<title>Iron Ember — Business Card</title>
<link href="https://fonts.googleapis.com/css2?family=Montserrat:wght@400;600;700&display=swap" rel="stylesheet">
<style>
  :root {
    --backdrop: #3a3a3a;
    --card-light: #ffffff;
    --card-dark: #2a2a2a;
    --ink: #222222;
    --ink-soft: #444444;
    --rule: #8a8a8a;
    --paper-text: #f4f4f4;
  }
  html, body {
    margin: 0;
    padding: 0;
    width: 1200px;
    height: 1200px;
    overflow: hidden;
    background: var(--backdrop);
    font-family: "Montserrat", Arial, sans-serif;
  }
  .canvas {
    position: relative;
    width: 1200px;
    height: 1200px;
  }
  .card {
    position: absolute;
    left: 180px;
    width: 840px;
    height: 480px;
    border-radius: 40px;
    overflow: hidden;
    box-shadow: 0 14px 30px rgba(0,0,0,0.35);
  }
  .card--front { top: 75px; background: var(--card-light); }
  .card--back { top: 645px; background: var(--card-dark); }

  /* Front */
  .contact {
    position: absolute;
    left: 70px;
    bottom: 70px;
    color: var(--ink);
  }
  .contact__name {
    margin: 0;
    font-size: 34px;
    font-weight: 700;
    letter-spacing: -0.5px;
    line-height: 1;
  }
  .contact__role {
    margin: 4px 0 18px;
    font-size: 17px;
    font-weight: 400;
    color: var(--ink-soft);
    letter-spacing: 0.5px;
  }
  .contact__list {
    list-style: none;
    margin: 0;
    padding: 0;
    font-size: 17px;
    line-height: 1.35;
  }
  .contact__item {
    display: flex;
    align-items: flex-start;
    gap: 10px;
  }
  .contact__icon {
    width: 18px;
    height: 18px;
    flex: none;
    margin-top: 2px;
    fill: var(--ink);
  }
  .divider {
    position: absolute;
    left: 440px;
    top: 120px;
    width: 1px;
    height: 200px;
    background: var(--rule);
  }
  .brand-front {
    position: absolute;
    left: 470px;
    right: 40px;
    top: 150px;
    display: flex;
    align-items: center;
    justify-content: center;
    gap: 14px;
    color: var(--ink);
  }
  .brand-front__dot {
    width: 30px;
    height: 30px;
    border-radius: 50%;
    background: var(--ink);
  }
  .brand-front__name {
    font-size: 40px;
    font-weight: 700;
    letter-spacing: 2px;
  }
  .front-tab {
    position: absolute;
    bottom: 0;
    left: 400px;
    width: 360px;
    height: 24px;
    background: var(--card-dark);
  }

  /* Back */
  .brand-back {
    position: absolute;
    inset: 0;
    display: flex;
    flex-direction: column;
    align-items: center;
    justify-content: center;
    gap: 28px;
    color: var(--paper-text);
  }
  .brand-back__dot {
    width: 40px;
    height: 40px;
    border-radius: 50%;
    background: var(--paper-text);
  }
  .brand-back__name {
    font-size: 30px;
    font-weight: 700;
    letter-spacing: 26px;
    padding-left: 26px;
  }
</style>
</head>
<body>
<main class="canvas">
  <section class="card card--front">
    <div class="contact">
      <h1 class="contact__name">FULL NAME</h1>
      <p class="contact__role">POSITION</p>
      <ul class="contact__list">
        <li class="contact__item">
          <svg class="contact__icon" viewBox="0 0 24 24"><path d="M6.6 10.8a15.1 15.1 0 0 0 6.6 6.6l2.2-2.2a1 1 0 0 1 1-.25 11.4 11.4 0 0 0 3.6.57 1 1 0 0 1 1 1V20a1 1 0 0 1-1 1A17 17 0 0 1 3 4a1 1 0 0 1 1-1h3.5a1 1 0 0 1 1 1c0 1.25.2 2.45.57 3.6a1 1 0 0 1-.25 1z"/></svg>
          <span>(000) 000 0000</span>
        </li>
        <li class="contact__item">
          <svg class="contact__icon" viewBox="0 0 24 24"><path d="M2 5h20v14H2z M4 7v.5l8 5 8-5V7l-8 5z" fill-rule="evenodd"/></svg>
          <span>email@company.com</span>
        </li>
        <li class="contact__item">
          <svg class="contact__icon" viewBox="0 0 24 24"><path d="M12 2a10 10 0 1 0 0 20 10 10 0 0 0 0-20zm6.9 6h-2.9a15.7 15.7 0 0 0-1.4-3.6A8 8 0 0 1 18.9 8zM12 4c.8 1.2 1.5 2.5 1.9 4h-3.8c.4-1.5 1.1-2.8 1.9-4zM4.3 14a8.2 8.2 0 0 1 0-4h3.4a16.5 16.5 0 0 0 0 4zm.8 2h2.9c.3 1.3.8 2.5 1.4 3.6A8 8 0 0 1 5.1 16zM8 8H5.1a8 8 0 0 1 4.3-3.6C8.8 5.5 8.3 6.7 8 8zm4 12c-.8-1.2-1.5-2.5-1.9-4h3.8c-.4 1.5-1.1 2.8-1.9 4zm2.3-6H9.7a14.7 14.7 0 0 1 0-4h4.6a14.7 14.7 0 0 1 0 4zm.3 5.6c.6-1.1 1.1-2.3 1.4-3.6h2.9a8 8 0 0 1-4.3 3.6zM16.3 14a16.5 16.5 0 0 0 0-4h3.4a8.2 8.2 0 0 1 0 4z"/></svg>
          <span>www.company.com</span>
        </li>
        <li class="contact__item">
          <svg class="contact__icon" viewBox="0 0 24 24"><path d="M12 2a7 7 0 0 0-7 7c0 5.2 7 13 7 13s7-7.8 7-13a7 7 0 0 0-7-7zm0 9.5a2.5 2.5 0 1 1 0-5 2.5 2.5 0 0 1 0 5z"/></svg>
          <span>123 Name Street, 000<br>Your City, 00000-000</span>
        </li>
      </ul>
    </div>
    <div class="divider"></div>
    <div class="brand-front">
      <span class="brand-front__dot"></span>
      <span class="brand-front__name">IRON EMBER</span>
    </div>
    <div class="front-tab"></div>
  </section>

  <section class="card card--back">
    <div class="brand-back">
      <span class="brand-back__dot"></span>
      <span class="brand-back__name">IRON EMBER</span>
    </div>
  </section>
</main>
</body>
</html>
```